Business Card Design Project : Tidewell Press

In preparation for market launch, Whistler's Tidewell Press require the development of a business card. Tidewell Press is a Community online publishing web portal. We provide the the city of Whistler located in B.C. (Canada) business directories, News, Classified ads, News, Events and blogs etc.

The main focus of the brand is to help local businesses to corporate with their online advertisement and marketing. Meeting our clients face to face is a must (B2B).

Target Market(s)

The target market is B2B customers. Business Owners to Marketing, advertising Managers

Industry/Entity Type

Business

Requirements
Must have
• - The business card will be two sided.
the BACK side will have our logo which consist of (icon, url,slogan) submited. The logo will be middle and centred.

The FRONT side should have company details:

Company Legal Name: FERNDALE TIDEWELL PRESS

Owen Marsk
Director of Sales & Marketing

www.ferndaletidewell.biz
owen@ferndaletidewell.biz

Phone: 555 014 3826
#2817 - 562 E. Harlow Ave.
Vancouver, B.C. K7P2R4 Canada
Nice to have
• - For the "FRONT" side of our business card. You can separate or re-arrange with our logo components (icon, logo,slogan). It does not have to be together.

Also our company legal name is rather long so arrange or organize the name in a way to make it shorter. Your experience and creativity will have to come in play.
Should not have
• should not have other colors beside logo color and black text (2 colors). Also nothing Three dimensional

```html
<!DOCTYPE html>
<html lang="en">
<head>
<meta charset="utf-8">
<title>Tidewell Press – Business Card</title>
<link rel="stylesheet" href="https://fonts.googleapis.com/css2?family=Open+Sans:wght@400;600;700&display=swap">
<style>
  :root {
    --page: #ecebe8;
    --card: #0c0c0d;
    --brand-blue: #1f7cc4;
    --rule-silver: #b9bcc0;
    --text-light: #f2f2f2;
    --font-main: "Open Sans", Arial, sans-serif;
  }
  * { box-sizing: border-box; margin: 0; padding: 0; }
  html, body {
    width: 756px; height: 1200px; overflow: hidden;
    background: var(--page);
    font-family: var(--font-main);
  }
  .sheet {
    width: 756px; height: 1200px;
    display: flex; flex-direction: column; align-items: center; justify-content: center;
    gap: 70px;
  }
  .card {
    position: relative;
    width: 660px; height: 377px;
    background: var(--card);
    overflow: hidden;
    box-shadow: 0 4px 14px rgba(0,0,0,.18);
  }

  /* Back side */
  .back__brand {
    position: absolute; top: 78px; left: 0; right: 0;
    text-align: center; color: var(--brand-blue);
  }
  .back__name {
    display: inline-flex; align-items: center; gap: 16px;
    font-size: 44px; font-weight: 700; letter-spacing: .5px;
  }
  .brand-dot {
    flex: none;
    width: 26px; height: 26px; border-radius: 50%;
    background: var(--brand-blue);
  }
  .back__slogan {
    margin-top: 14px;
    font-size: 26px; font-weight: 400;
  }
  .back__rule {
    position: absolute; left: 0; right: 0; top: 262px;
    height: 6px; background: var(--rule-silver);
  }
  .back__band {
    position: absolute; left: 0; right: 0; top: 268px;
    height: 66px; background: var(--brand-blue);
    display: flex; align-items: center; justify-content: center;
    color: var(--text-light); font-size: 22px; letter-spacing: .3px;
  }

  /* Front side */
  .front__identity {
    position: absolute; left: 30px; top: 156px; width: 254px;
    color: var(--brand-blue);
  }
  .front__slogan { font-size: 15px; margin-bottom: 8px; display: flex; align-items: center; gap: 10px; }
  .front__slogan .brand-dot { width: 14px; height: 14px; }
  .front__company { font-size: 18.5px; font-weight: 700; line-height: 1.2; white-space: nowrap; }
  .front__divider {
    position: absolute; left: 296px; top: 46px;
    width: 2px; height: 212px; background: var(--brand-blue);
  }
  .front__details {
    position: absolute; left: 324px; top: 42px; right: 24px;
    color: var(--text-light);
  }
  .person__name { color: var(--brand-blue); font-size: 26px; font-weight: 700; line-height: 1.1; }
  .person__title { font-size: 15px; margin-top: 4px; }
  .contact { list-style: none; font-size: 13.5px; line-height: 1.35; }
  .contact--address { margin-top: 36px; }
  .contact--lines { margin-top: 34px; }
  .contact li { display: flex; align-items: center; gap: 14px; margin-bottom: 6px; }
  .contact svg { flex: none; width: 18px; height: 18px; }
</style>
</head>
<body>
<main class="sheet">

  <section class="card card--back" aria-label="Card back">
    <div class="back__brand">
      <div class="back__name"><span class="brand-dot"></span>Tidewell Press</div>
      <p class="back__slogan">Your Community Portal</p>
    </div>
    <div class="back__rule"></div>
    <div class="back__band">www.ferndaletidewell.biz</div>
  </section>

  <section class="card card--front" aria-label="Card front">
    <div class="front__identity">
      <p class="front__slogan"><span class="brand-dot"></span>Your Community Portal</p>
      <p class="front__company">Ferndale Tidewell Press</p>
    </div>

    <div class="front__divider"></div>

    <div class="front__details">
      <p class="person__name">Owen Marsk</p>
      <p class="person__title">Director of Sales &amp; Marketing</p>

      <ul class="contact contact--address">
        <li>
          <svg viewBox="0 0 18 18" aria-hidden="true"><rect width="18" height="18" fill="#1f7cc4"/><path d="M3 9.5 9 4l6 5.5h-2V14h-3v-3H8v3H5V9.5z" fill="#0c0c0d"/></svg>
          <span>#2817 - 562 E. Harlow Ave.<br>Vancouver, B.C. K7P2R4 Canada</span>
        </li>
      </ul>

      <ul class="contact contact--lines">
        <li>
          <svg viewBox="0 0 18 18" aria-hidden="true"><circle cx="9" cy="9" r="9" fill="#1f7cc4"/><path d="M6 4.5c.6-.3 1.1 0 1.4.6l.6 1.3c.2.5 0 .9-.4 1.2l-.4.3c.4 1 1.2 1.9 2.2 2.4l.4-.4c.3-.4.8-.5 1.2-.3l1.3.6c.6.3.8.9.5 1.4-.5 1-1.6 1.4-2.7 1-2.6-.9-4.500-2.9-5.300-5.5C4.5 6 5 5 6 4.5z" fill="#0c0c0d"/></svg>
          <span>555 014 3826</span>
        </li>
        <li>
          <svg viewBox="0 0 18 18" aria-hidden="true"><rect x="1" y="4" width="16" height="10" fill="#1f7cc4"/><path d="M1 4l8 6 8-6" fill="none" stroke="#0c0c0d" stroke-width="1.4"/></svg>
          <span>owen@ferndaletidewell.biz</span>
        </li>
        <li>
          <svg viewBox="0 0 18 18" aria-hidden="true"><circle cx="9" cy="9" r="9" fill="#1f7cc4"/><g fill="none" stroke="#0c0c0d" stroke-width="1.2"><circle cx="9" cy="9" r="5.5"/><ellipse cx="9" cy="9" rx="2.4" ry="5.5"/><path d="M3.5 9h11"/></g></svg>
          <span>www.ferndaletidewell.biz</span>
        </li>
      </ul>
    </div>
  </section>

</main>
</body>
</html>
```